Business Card Design Project

Looking to update our business cards. We have a logo with our slogan. We are an IT firm so we wouldlike a modern look.

Industry/Entity Type

Business

```html
<!DOCTYPE html>
<html lang="en">
<head>
<meta charset="utf-8">
<title>Nodewell Inc – Business Card</title>
<link href="https://fonts.googleapis.com/css2?family=Jost:wght@400;500&display=swap" rel="stylesheet">
<style>
  :root{
    --lime:#9cbb2e;
    --olive:#5f7e2c;
    --ink:#222222;
    --paper:#f4f4f2;
    --stage:#d9d9d7;
    --white:#ffffff;
  }
  *{margin:0;padding:0;box-sizing:border-box}
  html,body{width:1200px;height:1008px;overflow:hidden;background:var(--white);font-family:"Jost",sans-serif}
  .stage{position:absolute;left:0;top:0;width:1200px;height:773px;background:var(--stage)}
  .rule{position:absolute;left:0;top:773px;width:1200px;height:9px;background:var(--lime)}
  .card{position:absolute;top:250px;width:480px;height:274px;overflow:hidden;box-shadow:0 6px 18px rgba(0,0,0,.18)}
  .card--front{left:90px;background:var(--lime);color:var(--white)}
  .card--back{left:630px;background:var(--paper);color:var(--ink)}
  .brand{position:absolute;left:0;right:0;top:96px;display:flex;align-items:center;justify-content:center;gap:12px;white-space:nowrap}
  .brand__dot{width:18px;height:18px;border-radius:50%;background:var(--white);flex:none}
  .brand__name{font-size:40px;font-weight:400;letter-spacing:6px;line-height:1}
  .brand__tagline{position:absolute;left:0;right:0;top:152px;text-align:center;font-size:14px;letter-spacing:4px;text-transform:uppercase;white-space:nowrap}
  .holder{position:absolute;left:150px;top:38px}
  .holder__name{font-size:40px;font-weight:500;letter-spacing:8px;color:var(--olive);line-height:1;white-space:nowrap}
  .holder__role{font-size:14px;letter-spacing:3px;font-weight:500;text-align:right;margin-top:4px;margin-right:8px}
  .band{position:absolute;left:0;width:480px;background:var(--lime)}
  .band--contact{top:134px;height:12px}
  .band--address{top:222px;height:26px;display:flex;align-items:center;padding-left:90px;font-size:12px;letter-spacing:2px;font-weight:500;white-space:nowrap}
  .icon{position:absolute;top:121px;width:38px;height:38px;border-radius:50%;background:var(--ink);display:flex;align-items:center;justify-content:center}
  .icon svg{width:20px;height:20px}
  .contact{position:absolute;font-size:11px;letter-spacing:1.5px;white-space:nowrap}
  .contact--phone{left:30px;top:170px}
  .contact--email{left:240px;top:170px;transform:translateX(-50%)}
  .contact--web{right:22px;top:188px}
  .logo{position:absolute;left:40px;top:840px;color:var(--olive)}
  .logo__row{display:flex;align-items:center;gap:12px}
  .logo__dot{width:16px;height:16px;border-radius:50%;background:var(--olive)}
  .logo__name{font-size:44px;letter-spacing:8px;line-height:1}
  .logo__tagline{font-size:13px;letter-spacing:3px;text-transform:uppercase;color:var(--ink);margin-top:8px}
</style>
</head>
<body>
  <div class="stage">
    <section class="card card--front">
      <div class="brand">
        <span class="brand__name">NODEWELL INC</span>
        <span class="brand__dot"></span>
      </div>
      <p class="brand__tagline">Simple IT, Done Right</p>
    </section>

    <section class="card card--back">
      <div class="holder">
        <div class="holder__name">JOHN DOE</div>
        <div class="holder__role">SPECIALIST</div>
      </div>
      <div class="band band--contact"></div>
      <span class="icon" style="left:70px">
        <svg viewBox="0 0 24 24"><path fill="#fff" d="M6.6 10.8a15 15 0 0 0 6.6 6.6l2.2-2.2a1 1 0 0 1 1-.25 11.4 11.4 0 0 0 3.6.57 1 1 0 0 1 1 1V20a1 1 0 0 1-1 1A17 17 0 0 1 3 4a1 1 0 0 1 1-1h3.5a1 1 0 0 1 1 1c0 1.25.2 2.45.57 3.57a1 1 0 0 1-.25 1z"/></svg>
      </span>
      <span class="icon" style="left:221px">
        <svg viewBox="0 0 24 24" fill="none" stroke="#fff" stroke-width="1.8"><rect x="3" y="6" width="18" height="12"/><path d="M3 6l9 7 9-7"/></svg>
      </span>
      <span class="icon" style="left:372px">
        <svg viewBox="0 0 24 24" fill="none" stroke="#fff" stroke-width="1.6"><circle cx="12" cy="12" r="9"/><ellipse cx="12" cy="12" rx="4" ry="9"/><path d="M3 12h18M5 7h14M5 17h14"/></svg>
      </span>
      <span class="contact contact--phone">555.014.2288</span>
      <span class="contact contact--email">JOHNDOE@NODEWELL.COM</span>
      <span class="contact contact--web">WWW.NODEWELL.COM</span>
      <div class="band band--address">250 CIRCUIT AVENUE/DENVER, CO 80205</div>
    </section>
  </div>
  <div class="rule"></div>

  <div class="logo">
    <div class="logo__row">
      <span class="logo__name">NODEWELL INC</span>
      <span class="logo__dot"></span>
    </div>
    <p class="logo__tagline">Simple IT, Done Right</p>
  </div>
</body>
</html>
```